Corvanel Website Homepage

Committed to delivering quality content, quillmarkwords.example is a content providing company. Equipped with resourceful writers with industry experience, we promise to empower our clients with content that is tailor-made to address specific requirements of their target Audience.

We need a website home page and one internal page designed. It is very important that the page be laid out with SEO in mind. We like the idea of using five images as navigation to our services. The five major services we offer are:
• Web Content writing (articles, features, website copy etc)
• Business Content writing (Press release, mailers & flyers, brochure/catalog)
• Personal Content writing (blog, speech writing)
• Hire a writer/editor
• Proof reading and editing services
The sample template (http://demo7.layoutsample.example/wt_48207/index.html) included has five images in the first fold. Designer can choose the right image for each service and lay over the service name on the image. Please do not use flash ( We will use javascripts). We need to have a detailed right side nav as in the template for SEO reasons. There will be some marketing ad- copy below the main images. Followed by a 200 character SEO optimized text defining our services in further detail. Apart from these a designer is free to use his creativity. The name of the site will be http://www.quillmarkwords.example/. This name will need a logo too. Please include it as part of design. Corvanelcorp is the owner of quillmarkwords.example. We already have a logo for Corvanel that is attached here as a separate file.

We have some taglines that need to be incorporated in the home page and other pages.
Please provide link button for Home, About us, Services, Samples, Pricing, Clients, Career, Contact us.

Links can be given on TOP, Sideways and Bottom and in the drop down menu of services etc.

Reason: Hi

We have made our project guaranteed and extended deadline by 5 days so you get more time to complete our project.

Thanks and Regards,

Ravindra Kulkarni
Corvanelcorp

Target Market(s)

Product Marketing Companies - Mostly in US.
Media companies which publish articles on various subjects. Travel and Lifestyle related sites, Educational Websites, Government Websites, Health related websites,

Industry/Entity Type

Marketing

Requirements
Must have
• Color of Homepage should blend with sober mood of the content. Writing Services should get highlighted in such a way that any person serious about the business visiting the site get attracted to read on the details of our content services. Most space should be used for details of writing services and links for our various pages and services. Webpage should be downloaded in lowest possible time.
Nice to have
• We have some idea about the website layouts;-http://www.pagefoundry.example/website-templates/48207.html - layout of information http://www.pagefoundry.example/website-templates/47915.html - for kind of marketing http://demo7.layoutsample.example/wt_48592/index.html - for colors
we attach a word file representing our idea in some way but not limited to it.
Should not have
• Gaudy (aggressive dark) colors. It should not be cluttered. No flash.

```html
<!DOCTYPE html>
<html lang="en">
<head>
<meta charset="utf-8">
<title>Quillmarkwriter — Content Writing Services</title>
<link rel="stylesheet" href="https://fonts.googleapis.com/css2?family=Arimo:wght@400;700&family=Ubuntu:wght@400;500;700&family=Libre+Baskerville:wght@400;700&display=swap">
<style>
:root{
  --orange:#e8740c;
  --ink:#3a3a3a;
  --text:#4a4a4a;
  --muted:#6a6a6a;
  --rule:#9a9a9a;
  --dark-tab:#5a5a5a;
  --page-top:#dfe7ea;
  --page-bottom:#eeeeee;
  --panel:#ffffff;
  --box:#f6f6f6;
  --box-edge:#d9d9d9;
  --band:#e6e6e6;
  --brand-red:#c8312a;
}
*{box-sizing:border-box;margin:0;padding:0}
html,body{width:960px;height:1200px;overflow:hidden}
body{
  position:relative;
  background:linear-gradient(var(--page-top),var(--page-bottom) 320px,var(--page-bottom));
  font-family:"Arimo",Arial,sans-serif;color:var(--text);
}
a{color:inherit;text-decoration:none}
.abs{position:absolute}

.sheet{left:118px;top:34px;width:724px;height:890px;background:var(--panel);
  border-radius:12px;box-shadow:0 0 0 2px #e4e8ea}

.brand{left:142px;top:68px;font-family:"Ubuntu",sans-serif;font-size:29px;font-weight:400;color:var(--orange);letter-spacing:-.3px}

.search-field{left:577px;top:79px;width:172px;height:19px;border:1px solid #c9c9c9;background:#fff}
.search-btn{left:753px;top:78px;width:62px;height:20px;border:1px solid #c4c4c4;border-radius:4px;
  background:linear-gradient(#f7f7f7,#dcdcdc);font-size:11px;color:#555;text-align:center;line-height:18px}

.main-nav{left:143px;top:133px;width:674px;height:30px}
.main-nav a{position:absolute;top:2px;font-family:"Libre Baskerville",Georgia,serif;font-size:10.5px;
  font-weight:700;color:#6b6b6b;letter-spacing:.3px}
.main-nav a.current{color:#2b2b2b}
.nav-rule{left:143px;top:158px;width:674px;height:4px;background:#c9c9c9}
.nav-rule-active{left:143px;top:158px;width:86px;height:4px;background:var(--orange)}
.nav-pointer{left:182px;top:153px}
.nav-shadow{left:143px;top:162px;width:674px;height:18px;background:linear-gradient(#e9e9e9,rgba(255,255,255,0))}

.service-tile{top:194px;width:134px;height:240px;border:1px solid #c8c8c8;background:#eee;overflow:hidden}
.service-tile .photo{height:195px}
.service-tile .caption{position:absolute;left:0;right:0;top:195px;bottom:0;
  background:linear-gradient(#f4f4f4,#d6d6d6);border-top:1px solid #bbb;
  font-family:"Arimo",Arial,sans-serif;font-weight:700;font-size:14px;line-height:14.5px;
  letter-spacing:-.4px;color:#4a4a4a;text-align:right;padding:3px 4px 0 0}
.service-tile .caption::before{content:"";position:absolute;left:5px;top:-3px;width:19px;height:4px;background:var(--dark-tab)}
.service-tile.featured .caption{color:var(--orange)}

.band{left:137px;top:440px;width:690px;height:470px;background:linear-gradient(var(--band),#f7f7f7 90px,#fbfbfb)}

.box{border:1px solid var(--box-edge);background:linear-gradient(90deg,#fff,var(--box))}
.box-shadow{height:4px;background:#d2d2d2}

.welcome{left:144px;top:446px;width:457px;height:451px}
.welcome h1{position:absolute;left:18px;top:9px;font-family:"Ubuntu",sans-serif;font-weight:400;font-size:14px;color:#444}
.welcome h1 span{color:var(--orange)}
.welcome .title-rule{position:absolute;left:18px;top:27px;width:412px;height:1px;background:#8a8a8a}
.welcome .title-rule::after{content:"";position:absolute;right:-16px;top:-2px;width:16px;height:3px;background:var(--dark-tab)}
.lead{position:absolute;left:18px;top:36px;width:400px;font-family:"Ubuntu",sans-serif;font-weight:500;font-size:11px;line-height:18.5px;color:#3a3a3a}
.lead-rule{position:absolute;left:18px;top:78px;width:415px;height:1px;background:#cfcfcf}
.intro{position:absolute;left:18px;top:85px;width:418px;font-family:"Ubuntu",sans-serif;font-size:8.8px;line-height:18.4px;color:#444}

.service-list{position:absolute;left:17px;top:169px;width:420px;list-style:none}
.service-list li{position:relative;height:54px;padding-left:50px}
.service-list .thumb{position:absolute;left:0;top:1px;width:46px;height:46px;border:1px solid #aab;border-radius:4px}
.service-list h2{font-size:10.5px;font-weight:700;color:#3a3a3a;letter-spacing:-.2px;line-height:13px;padding-top:2px}
.service-list p{font-size:9px;line-height:14.4px;color:#555;margin-top:2px}
.service-list p a{color:var(--orange);font-weight:700}

.side-nav{left:618px;top:446px;width:197px;height:323px}
.side-heading{font-family:"Ubuntu",sans-serif;font-size:14px;color:var(--orange);text-align:right;font-weight:400}
.side-nav h3{position:absolute;right:12px;top:9px}
.side-nav ul{position:absolute;left:7px;top:32px;width:180px;list-style:none}
.side-nav li{text-align:right;font-size:10.5px;color:#555;letter-spacing:-.2px;padding-right:10px;position:relative}
.side-nav li::after{content:"";position:absolute;right:0;top:50%;margin-top:-3px;border:3px solid transparent;border-right:4px solid #555;border-left:0}
.side-nav li.group{font-weight:700;color:#3a3a3a}
.side-nav .divider{position:absolute;left:7px;width:180px;height:1px;background:#8a8a8a}
.side-nav .divider::before{content:"";position:absolute;left:0;top:-1px;width:15px;height:3px;background:var(--dark-tab)}

.news{left:618px;top:780px;width:197px;height:117px}
.news h3{position:absolute;right:12px;top:8px}
.news p{position:absolute;left:12px;top:34px;width:176px;font-family:"Ubuntu",sans-serif;font-size:8.8px;line-height:14.4px;color:#222}
.news p a{color:var(--orange)}

.footer-col{list-style:none;font-size:10.5px;line-height:18.4px;letter-spacing:-.2px}
.footer-col.primary{left:163px;top:943px;font-weight:700;color:#666}
.footer-col.secondary{left:274px;top:943px;color:#777}
.footer-col.secondary li:first-child{font-weight:700;color:#666}

.subscribe-heading{right:158px;top:942px}
.email-field{left:618px;top:965px;width:197px;height:24px;border:1px solid #cfcfcf;background:#fff;
  font-family:"Ubuntu",sans-serif;font-size:8.5px;color:#666;padding:6px 0 0 7px}
.social{top:997px;height:24px;border-radius:3px;background:#8fa6c3;color:#fff;font-size:6.5px;font-weight:700;
  text-align:center;line-height:24px}
.submit-btn{left:742px;top:997px;width:75px;height:22px;border:1px solid #bdbdbd;border-radius:5px;
  background:linear-gradient(#f8f8f8,#d9d9d9);font-family:"Ubuntu",sans-serif;font-size:10.5px;color:#555;text-align:center;line-height:20px}

.footer-rule{left:144px;top:1068px;width:672px;height:1px;background:#cfcfcf}
.legal{left:162px;top:1088px;font-size:10.5px;line-height:18.5px;color:#777}
.legal small{font-size:10px}
.owner{left:700px;top:1092px;display:flex;align-items:center;gap:8px;font-family:"Arimo",Arial,sans-serif;font-size:19px;color:var(--brand-red)}
.owner i{display:block;width:12px;height:12px;background:var(--brand-red)}
</style>
</head>
<body>

<div class="abs sheet"></div>

<header>
  <a class="abs brand" href="#">Quillmarkwriter</a>
  <form role="search">
    <div class="abs search-field" aria-label="Search"></div>
    <div class="abs search-btn">Search</div>
  </form>
  <nav class="abs main-nav">
    <a class="current" style="left:26px" href="#">HOME</a>
    <a style="left:95px" href="#">ABOUT US</a>
    <a style="left:183px" href="#">SERVICES</a>
    <a style="left:268px" href="#">SAMPLES</a>
    <a style="left:355px" href="#">PRICING</a>
    <a style="left:438px" href="#">CLIENTS</a>
    <a style="left:524px" href="#">CAREER</a>
    <a style="left:591px" href="#">CONTACT US</a>
  </nav>
  <div class="abs nav-shadow"></div>
  <div class="abs nav-rule"></div>
  <div class="abs nav-rule-active"></div>
  <svg class="abs nav-pointer" width="9" height="6" viewBox="0 0 9 6"><path d="M0 6 L4.5 0 L9 6Z" fill="#e8740c"/></svg>
</header>

<section aria-label="Writing services">
  <a class="abs service-tile" style="left:143px" href="#">
    <div class="photo" role="img" aria-label="Photo of a hand typing on a laptop keyboard" style="background:linear-gradient(160deg,#e9e9e9,#b9b9b9 55%,#8e8e8e)"></div>
    <div class="caption">Web Content<br>Writing</div>
  </a>
  <a class="abs service-tile featured" style="left:278px" href="#">
    <div class="photo" role="img" aria-label="Photo of a hand with a pen over business charts" style="background:linear-gradient(160deg,#dfe7ee,#b8c8d6 50%,#e7dccf)"></div>
    <div class="caption">Business Content<br>Writing</div>
  </a>
  <a class="abs service-tile" style="left:413px" href="#">
    <div class="photo" role="img" aria-label="Photo of hands reviewing a printed document" style="background:linear-gradient(160deg,#cfcfcf,#eeeeee 50%,#bdbdbd)"></div>
    <div class="caption">Personal Content<br>Writing</div>
  </a>
  <a class="abs service-tile" style="left:548px" href="#">
    <div class="photo" role="img" aria-label="Photo of a writer taking notes at a desk" style="background:linear-gradient(160deg,#e6e6e6,#3a3a3a 55%,#dcdcdc)"></div>
    <div class="caption">Hire a Writer/<br>Editor</div>
  </a>
  <a class="abs service-tile" style="left:683px" href="#">
    <div class="photo" role="img" aria-label="Photo of a hand proofreading with a pen" style="background:linear-gradient(160deg,#d8d8d8,#efe6dc 50%,#c9c9c9)"></div>
    <div class="caption">Proof Reading &amp;<br>Editing Services</div>
  </a>
  <div class="abs box-shadow" style="left:148px;top:433px;width:127px"></div>
  <div class="abs box-shadow" style="left:284px;top:433px;width:127px"></div>
  <div class="abs box-shadow" style="left:419px;top:433px;width:127px"></div>
  <div class="abs box-shadow" style="left:554px;top:433px;width:127px"></div>
  <div class="abs box-shadow" style="left:689px;top:433px;width:127px"></div>
</section>

<div class="abs band"></div>

<main class="abs box welcome">
  <h1>Welcome to <span>Quillmarkwords!</span></h1>
  <div class="title-rule"></div>
  <p class="lead">It is a long established fact that a reader will be distracted by the readable content of a page when looking at its layout.</p>
  <div class="lead-rule"></div>
  <p class="intro">Lorem Ipsum is simply dummy text of the printing and typesetting industry. Lorem Ipsum has been the industry's standard dummy text ever since the 1500s, when an unknown printer took a galley of type and scrambled it to make a type specimen book. It has survived not only five centuries, but also the leap into electronic typesetting, remaining essentially unchanged.</p>
  <ul class="service-list">
    <li><div class="thumb" role="img" aria-label="Laptop thumbnail photo" style="background:linear-gradient(160deg,#ddd,#8a7670)"></div>
      <h2>Web Content Writing</h2>
      <p>It is a long established fact that a reader will be distracted by the readable content of a page when looking at its layout. <a href="#">[Learn More...]</a></p></li>
    <li><div class="thumb" role="img" aria-label="Business charts thumbnail photo" style="background:linear-gradient(160deg,#c8d6e3,#e8ddd0)"></div>
      <h2>Business Content Writing</h2>
      <p>It is a long established fact that a reader will be distracted by the readable content of a page when looking at its layout. <a href="#">[Learn More...]</a></p></li>
    <li><div class="thumb" role="img" aria-label="Document review thumbnail photo" style="background:linear-gradient(160deg,#e9ddd3,#b08a70)"></div>
      <h2>Personal Content Writing</h2>
      <p>It is a long established fact that a reader will be distracted by the readable content of a page when looking at its layout. <a href="#">[Learn More...]</a></p></li>
    <li><div class="thumb" role="img" aria-label="Writer at desk thumbnail photo" style="background:linear-gradient(160deg,#c5d2e0,#2e3440)"></div>
      <h2>Hire a Writer | Content Editor</h2>
      <p>It is a long established fact that a reader will be distracted by the readable content of a page when looking at its layout. <a href="#">[Learn More...]</a></p></li>
    <li><div class="thumb" role="img" aria-label="Proofreading thumbnail photo" style="background:linear-gradient(160deg,#e4e4e4,#3b3b3b)"></div>
      <h2>Proof Reading &amp; Editing Services</h2>
      <p>It is a long established fact that a reader will be distracted by the readable content of a page when looking at its layout. <a href="#">[Learn More...]</a></p></li>
  </ul>
</main>
<div class="abs box-shadow" style="left:148px;top:896px;width:447px"></div>

<aside class="abs box side-nav">
  <h3 class="side-heading">Page Navigation</h3>
  <ul>
    <li class="group" style="position:absolute;right:0;top:0">About Us</li>
    <li class="group" style="position:absolute;right:0;top:25px">Services</li>
    <li style="position:absolute;right:0;top:43px;white-space:nowrap">Web Content Wrting</li>
    <li style="position:absolute;right:0;top:61px;white-space:nowrap">Business Content Wrting</li>
    <li style="position:absolute;right:0;top:79px;white-space:nowrap">Personal Content Wrting</li>
    <li style="position:absolute;right:0;top:97px;white-space:nowrap">Hire a Writer | Editor</li>
    <li style="position:absolute;right:0;top:115px;white-space:nowrap">Proof Reading &amp; Editing Services</li>
    <li class="group" style="position:absolute;right:0;top:141px">Samples</li>
    <li class="group" style="position:absolute;right:0;top:167px">Pricing</li>
    <li class="group" style="position:absolute;right:0;top:189px">Clients</li>
    <li class="group" style="position:absolute;right:0;top:213px">Career</li>
    <li class="group" style="position:absolute;right:0;top:236px">Contact Us</li>
  </ul>
  <div class="divider" style="top:51px"></div>
  <div class="divider" style="top:172px"></div>
  <div class="divider" style="top:197px"></div>
  <div class="divider" style="top:219px"></div>
  <div class="divider" style="top:243px"></div>
  <div class="divider" style="top:266px"></div>
</aside>
<div class="abs box-shadow" style="left:624px;top:768px;width:189px"></div>

<aside class="abs box news">
  <h3 class="side-heading">Latest News</h3>
  <p>The standard chunk of Lorem Ipsum used since the 1500s is reproduced below for those interested. <a href="#">[Read More...]</a></p>
</aside>
<div class="abs box-shadow" style="left:624px;top:896px;width:189px"></div>
<div class="abs box-shadow" style="left:138px;top:922px;width:668px;height:3px;background:#dcdcdc"></div>

<footer>
  <ul class="abs footer-col primary">
    <li>About Us</li><li>Samples</li><li>Pricing</li><li>Clients</li><li>Career</li><li>Contact Us</li>
  </ul>
  <ul class="abs footer-col secondary">
    <li>Services</li><li>Web Content Wrting</li><li>Business Content Wrting</li><li>Personal Content Wrting</li><li>Hire a Writer | Editor</li><li>Proof Reading &amp; Editing Services</li>
  </ul>
  <h3 class="abs side-heading subscribe-heading">Subscribe Newsletter</h3>
  <div class="abs email-field">Type your e-mail here...</div>
  <a class="abs social" style="left:676px;width:24px" href="#">Linkfold</a>
  <a class="abs social" style="left:707px;width:24px;background:#8ebfd2" href="#">Chirper</a>
  <div class="abs submit-btn">Submit</div>

  <div class="abs footer-rule"></div>
  <p class="abs legal">Copyright © 2011 Quillmarkwriter. All rights reserved.<br><small>Privacy Policy | Terms of Service</small></p>
  <div class="abs owner"><i></i>Corvanel</div>
</footer>

</body>
</html>
```